Building company buisness cards

We are looking for a sharp modern new look for our business cards.
We are a New Zealand based company that specialises in house and land packages.
We have attached a photo of the current logo and would like to see if it can be improved somehow if needed.
We are open to any colours but we have chosen green at this stage.
Feel free to change the font and make the logo smarter looking.
Play with the colours and see what looks best.

We want a card that looks so good know one will want to throw it away!

Target Market(s)

Home buyers

Industry/Entity Type

Building

Contact Information for Business Card

Dorian Keswick
0217392604
dkeswick@tidewellhomecraft.co.nz
tidewellhomecraft.co.nz

Font styles to use
Serif
Sans Serif

Colors

Designer to choose colors to be used in the design.

Requirements
Must have
• Logo and company name on one side, details on the other side
Nice to have
• Color codes for the original green are HEX #4a8028, RGB(74,128,40), CMYK(42,0,69,50)
• Round corners, Raised and/or spot UV

```html
<!DOCTYPE html>
<html lang="en">
<head>
<meta charset="utf-8">
<title>Tidewell Homecraft – Business Card</title>
<link rel="stylesheet" href="https://fonts.googleapis.com/css2?family=Montserrat:wght@600;700;800&display=swap">
<style>
  :root {
    --brand-green: #5e7f45;
    --pattern-tint-a: #f1f4ee;
    --pattern-tint-b: #e8ede3;
    --card-white: #fbfbfa;
    --backdrop: #e4e5e4;
    --text-white: #ffffff;
  }
  * { margin: 0; padding: 0; box-sizing: border-box; }
  html, body {
    width: 1200px; height: 800px; overflow: hidden;
    background: var(--backdrop);
    font-family: "Montserrat", Arial, sans-serif;
  }
  .canvas {
    width: 1200px; height: 800px;
    display: flex; align-items: center; justify-content: center; gap: 40px;
  }
  .card {
    position: relative;
    width: 540px; height: 309px;
    background: var(--card-white);
    border-radius: 14px;
    overflow: hidden;
    box-shadow: 0 6px 18px rgba(0,0,0,0.12);
  }
  .pattern-area {
    position: absolute; inset: 0;
    background: linear-gradient(135deg, var(--pattern-tint-a), var(--pattern-tint-b));
  }

  /* front */
  .front-brand {
    position: absolute; inset: 0;
    display: flex; flex-direction: column; align-items: center; justify-content: center;
    color: var(--brand-green);
    font-weight: 800; font-size: 56px; line-height: 1; letter-spacing: -0.5px;
    text-align: center;
  }
  .front-brand .mark-dot {
    width: 40px; height: 40px; border-radius: 50%;
    background: var(--brand-green); margin-bottom: 16px;
  }

  /* back */
  .back-top {
    position: absolute; left: 0; right: 0; top: 0; height: 170px;
    display: flex; flex-direction: column; align-items: center; justify-content: center;
    color: var(--brand-green); text-align: center;
  }
  .back-brand {
    display: flex; flex-direction: column; align-items: center;
    font-weight: 800; font-size: 18px; line-height: 1.05;
  }
  .back-brand .mark-dot {
    width: 14px; height: 14px; border-radius: 50%;
    background: var(--brand-green); margin-bottom: 6px;
  }
  .person-name {
    margin-top: 14px;
    font-weight: 800; font-size: 32px; line-height: 1; letter-spacing: 0.3px;
  }
  .contact-band {
    position: absolute; left: 0; right: 0; bottom: 0; height: 139px;
    background: var(--brand-green);
    color: var(--text-white);
    display: flex; flex-direction: column; align-items: center; justify-content: center; gap: 6px;
    font-weight: 700; font-size: 19px; line-height: 1.1; text-align: center;
  }
  .contact-band .phone { font-size: 21px; letter-spacing: 1px; }
</style>
</head>
<body>
<main class="canvas">

  <section class="card card-front" aria-label="Card front">
    <div class="pattern-area" role="img" aria-label="Faint repeating company-name pattern in pale green"></div>
    <div class="front-brand">
      <div class="mark-dot"></div>
      <div>tidewell</div>
      <div>homecraft.</div>
    </div>
  </section>

  <section class="card card-back" aria-label="Card back">
    <div class="pattern-area" role="img" aria-label="Faint repeating company-name pattern in pale green"></div>
    <div class="back-top">
      <div class="back-brand">
        <span class="mark-dot"></span>
        <span>tidewell</span>
        <span>homecraft.</span>
      </div>
      <div class="person-name">Dorian Keswick</div>
    </div>
    <div class="contact-band">
      <div class="phone">0217392604</div>
      <div class="email">dkeswick@tidewellhomecraft.co.nz</div>
      <div class="web">tidewellhomecraft.co.nz</div>
    </div>
  </section>

</main>
</body>
</html>
```